Parcelnook.com.au Front page Re-Design

We need a front page redesign for the website parcelnook.com.au,
The site needs to keep a number of products products highlighted on the front page. Same buttons but navigation could be different and we still need some text for SEO.
What we do not currently like:
1. The big banners.
2. The use of too much orange especially the 50% orange borders.
3. the fact that products cannot be seen straight away when logged-in.
4. The fact that it is hard to convert to tablet friendly
5. The fact that it's not a modern design.

What we think we want:

1. Maybe more use of 1 colour (purple or orange) with the other a secondary highlight colour.
2. A more modern look
3. The wow factor

Look at parcelnook.com.au take the elements that you need and design.
Updates

Reason: Designs are getting better. liking the designs that don't look like the usual e-commerce templates out there.

Hello,

We are making decisions next Monday. Sorry for the delay but there has been a lot of holidays in Australia and decision makers away.

Industry/Entity Type

Seo

Colors
6b449b
f78f20
ffffff

```html
<!DOCTYPE html>
<html lang="en">
<head>
<meta charset="utf-8">
<title>Parcelnook.com.au – Easter Egg Hunt</title>
<link href="https://fonts.googleapis.com/css2?family=Open+Sans:wght@400;600;700&display=swap" rel="stylesheet">
<style>
  :root {
    --purple: #6b449b;
    --orange: #f78f20;
    --white: #ffffff;
    --sidebar-bg: #ebebec;
    --ink: #1e1e1e;
    --muted: #8a8a8a;
    --line: #d9d9d9;
    --green: #2f9a2f;
    --card-border: #d4d4d4;
  }
  * { box-sizing: border-box; margin: 0; padding: 0; }
  html, body { width: 826px; height: 1200px; overflow: hidden; background: var(--white); }
  body { position: relative; font-family: "Open Sans", Arial, sans-serif; color: var(--ink); }
  .abs { position: absolute; }

  /* Sidebar */
  .sidebar { position: absolute; left: 0; top: 0; width: 159px; height: 1200px; background: var(--sidebar-bg); }
  .brand { position: absolute; left: 17px; top: 18px; display: flex; align-items: center; gap: 6px; }
  .brand-mark { width: 20px; height: 20px; background: var(--orange); }
  .brand-name { font-size: 15px; font-weight: 700; color: var(--purple); letter-spacing: -0.3px; }
  .brand-tagline { position: absolute; left: 17px; top: 62px; font-size: 8px; color: var(--purple); }
  .search { position: absolute; left: 18px; top: 91px; width: 123px; height: 24px; border: 1px solid #cfcfcf; border-radius: 12px; background: var(--white); font-size: 8px; color: var(--muted); padding: 6px 0 0 34px; }
  .search svg { position: absolute; left: 13px; top: 6px; }
  .nav { position: absolute; left: 17px; top: 0; width: 124px; }
  .nav-item { position: absolute; left: 0; width: 124px; font-size: 8px; text-transform: uppercase; color: var(--ink); display: flex; justify-content: space-between; align-items: center; }
  .nav-item .count { color: var(--muted); font-size: 8px; }
  .nav-item.sub { left: 22px; width: 102px; text-transform: none; }
  .nav-item.active, .nav-item.sub.active span:first-child { color: var(--orange); }
  .nav-item.sub.active span:first-child { text-decoration: underline; }
  .caret { display: inline-block; margin-left: 6px; width: 0; height: 0; border-top: 3px solid transparent; border-bottom: 3px solid transparent; border-left: 4px solid var(--ink); }
  .caret.down { border-left: 3px solid transparent; border-right: 3px solid transparent; border-top: 4px solid var(--orange); border-bottom: 0; }
  .side-rule { position: absolute; left: 17px; width: 124px; height: 1px; background: #d7d7d7; }
  .cart { position: absolute; left: 17px; top: 434px; width: 124px; display: flex; justify-content: space-between; font-size: 8px; }
  .cart .count { color: var(--muted); }
  .side-links { position: absolute; left: 24px; top: 472px; font-size: 6.5px; color: var(--muted); word-spacing: 4px; letter-spacing: 0.2px; }
  .cards { position: absolute; left: 18px; top: 498px; display: flex; gap: 4px; }
  .cards span { width: 18px; height: 11px; border-radius: 2px; border: 1px solid #cfcfcf; background: var(--white); }

  /* Hero */
  .hero { position: absolute; left: 159px; top: 0; width: 667px; height: 382px; overflow: hidden;
    background:
      radial-gradient(ellipse 260px 160px at 430px 20px, rgba(170,190,120,0.8), transparent 70%),
      radial-gradient(ellipse 200px 150px at 640px 40px, rgba(150,200,80,0.9), transparent 70%),
      radial-gradient(ellipse 300px 200px at 100px 330px, rgba(140,90,190,0.85), transparent 70%),
      radial-gradient(ellipse 260px 180px at 580px 260px, rgba(40,40,40,0.9), transparent 70%),
      linear-gradient(135deg, #4a3f56 0%, #5a3d78 45%, #2e2a2e 100%); }
  .hero-title { position: absolute; left: 0; width: 667px; top: 48px; text-align: center; font-size: 44px; font-weight: 700; color: var(--white); letter-spacing: -0.5px; }
  .hero-sub { position: absolute; left: 0; width: 667px; top: 112px; text-align: center; font-size: 11.5px; color: var(--white); }
  .ribbon { position: absolute; right: 0; top: 0; }
  .product-ring { position: absolute; top: 165px; width: 140px; height: 140px; border-radius: 50%; background: rgba(30,25,35,0.75); }
  .product-ring .photo { position: absolute; left: 15px; top: 15px; width: 110px; height: 110px; border-radius: 50%; background: radial-gradient(circle at 50% 50%, #f4f1f7 40%, #ddd4ea 100%); border: 1px solid #fff; }
  .hero-name { position: absolute; top: 323px; width: 140px; text-align: center; font-size: 8.5px; font-weight: 600; color: var(--white); }
  .hero-link { position: absolute; top: 339px; width: 140px; text-align: center; font-size: 8px; color: #a9a3ae; }

  /* Occasions */
  .occasion { position: absolute; top: 406px; width: 200px; text-align: center; }
  .occasion-icon { margin: 0 auto; width: 48px; height: 48px; border-radius: 50%; border: 1px solid #cfcfcf; display: flex; align-items: center; justify-content: center; }
  .occasion-title { margin-top: 9px; font-size: 11px; }
  .occasion-link { font-size: 8px; color: var(--orange); margin-top: 1px; }
  .occasion-text { font-size: 8.5px; line-height: 14px; margin-top: 4px; }
  .rule { position: absolute; left: 177px; width: 631px; height: 1px; background: var(--line); }

  /* Products */
  .product { position: absolute; width: 189px; }
  .product-frame { width: 189px; height: 152px; border: 2px solid var(--card-border); background: var(--white); display: flex; align-items: center; justify-content: center; }
  .product-photo { width: 100px; height: 120px; }
  .product-row { display: flex; justify-content: space-between; margin-top: 4px; font-size: 8px; }
  .product-price { color: var(--muted); }
  .product-meta { display: flex; justify-content: space-between; font-size: 6.5px; margin-top: 2px; text-transform: uppercase; color: #777; }
  .product-meta .ship { color: var(--green); font-weight: 700; }

  /* SEO block */
  .seo { position: absolute; left: 177px; top: 1004px; width: 310px; }
  .seo h2 { font-size: 11px; font-weight: 700; }
  .seo p { font-size: 8px; line-height: 17px; margin-top: 3px; }
  .seo-photo { position: absolute; top: 988px; width: 116px; height: 116px; border-radius: 50%; }

  /* Footer */
  .footer-links { position: absolute; left: 159px; width: 667px; top: 1133px; text-align: center; font-size: 6.5px; color: var(--orange); word-spacing: 2px; }
  .footer-links span { margin: 0 5px; }
  .copyright { position: absolute; left: 159px; width: 667px; top: 1144px; text-align: center; font-size: 6.5px; color: #666; }
  .footer-band { position: absolute; left: 159px; top: 1176px; width: 667px; height: 24px; background: var(--purple); }
</style>
</head>
<body>

<aside class="sidebar">
  <div class="brand"><span class="brand-mark"></span><span class="brand-name">parcelnook.com.au</span></div>
  <div class="brand-tagline">parcel &amp; hamper network</div>

  <div class="search">
    <svg width="11" height="11" viewBox="0 0 11 11"><circle cx="4.5" cy="4.5" r="3.5" fill="none" stroke="#666" stroke-width="1.3"/><line x1="7" y1="7" x2="10" y2="10" stroke="#666" stroke-width="1.3"/></svg>
    Search Store
  </div>

  <nav class="nav">
    <div class="nav-item" style="top:144px"><span>By Occasion<i class="caret"></i></span><span class="count">645</span></div>
    <div class="nav-item" style="top:169px"><span>By Special Event<i class="caret"></i></span><span class="count">398</span></div>
    <div class="nav-item active" style="top:193px"><span>By Price<i class="caret down"></i></span><span class="count">687</span></div>
    <div class="nav-item sub" style="top:218px"><span>Under $50</span><span class="count">324</span></div>
    <div class="nav-item sub active" style="top:242px"><span>$50 - $70</span><span class="count">173</span></div>
    <div class="nav-item sub" style="top:267px"><span>$75 - $100</span><span class="count">68</span></div>
    <div class="nav-item sub" style="top:291px"><span>Over $100</span><span class="count">122</span></div>
    <div class="nav-item" style="top:316px"><span>By Basket Style<i class="caret"></i></span><span class="count">265</span></div>
    <div class="nav-item" style="top:340px"><span>For Him</span><span class="count">97</span></div>
    <div class="nav-item" style="top:365px"><span>For Her</span><span class="count">114</span></div>
    <div class="nav-item" style="top:389px"><span>All</span><span class="count">5758</span></div>
  </nav>

  <div class="side-rule" style="top:416px"></div>
  <div class="cart"><span>Your cart</span><span class="count">0 items</span></div>
  <div class="side-rule" style="top:457px"></div>
  <div class="side-links">CONTACT SHIPPING PRIVACY</div>
  <div class="cards"><span></span><span></span><span></span><span></span><span></span><span></span></div>
</aside>

<section class="hero">
  <h1 class="hero-title">Easter Egg Hunt</h1>
  <p class="hero-sub">Get your easter gift and eggs only at Parcelnook.com.au</p>

  <svg class="ribbon" width="110" height="95" viewBox="0 0 110 95">
    <polygon points="20,0 110,0 110,95" fill="var(--orange)" fill-opacity="0"/>
    <polygon points="28,0 58,0 110,52 110,82" fill="var(--orange)"/>
    <text x="0" y="0" transform="translate(76,18) rotate(45)" fill="#fff" font-family="Open Sans, sans-serif" font-size="7" font-weight="700" text-anchor="middle">FREE SHIPPING</text>
    <text x="0" y="0" transform="translate(72,30) rotate(45)" fill="#fff" font-family="Open Sans, sans-serif" font-size="5.5" font-weight="600" text-anchor="middle">ON EVERYTHING!</text>
  </svg>

  <div class="product-ring" style="left:98px"><div class="photo" role="img" aria-label="Teddy bear with wrapped easter eggs in a tin"></div></div>
  <div class="product-ring" style="left:208px"><div class="photo" role="img" aria-label="Clear tin with rabbit and easter eggs tied with blue ribbon"></div></div>
  <div class="product-ring" style="left:318px"><div class="photo" role="img" aria-label="Yellow bear with colourful wrapped easter eggs"></div></div>
  <div class="product-ring" style="left:428px"><div class="photo" role="img" aria-label="Blue plush bunny box with easter eggs"></div></div>

  <div class="hero-name" style="left:98px">Thomas Bear Easter Tin</div>
  <div class="hero-link" style="left:98px">View Product</div>
  <div class="hero-name" style="left:208px">Hopper Rabbit Easter Tin</div>
  <div class="hero-link" style="left:208px">View Product</div>
  <div class="hero-name" style="left:318px">Big Bear Easter Gift</div>
  <div class="hero-link" style="left:318px">View Product</div>
  <div class="hero-name" style="left:428px">Blue Bunny Easter Box</div>
  <div class="hero-link" style="left:428px">View Product</div>
</section>

<section>
  <div class="occasion" style="left:179px">
    <div class="occasion-icon">
      <svg width="20" height="20" viewBox="0 0 20 20"><ellipse cx="9" cy="13" rx="6" ry="4.5" fill="var(--orange)"/><circle cx="14" cy="8" r="3" fill="var(--orange)"/><ellipse cx="14" cy="3.5" rx="1" ry="3" fill="var(--orange)"/><ellipse cx="16" cy="4" rx="1" ry="3" fill="var(--orange)"/></svg>
    </div>
    <div class="occasion-title">Easter</div>
    <div class="occasion-link">View all easter gifts</div>
    <div class="occasion-text">Ut congue ut lectus a lobortis<br>aenean iaculis sem est,</div>
  </div>
  <div class="occasion" style="left:393px">
    <div class="occasion-icon">
      <svg width="20" height="20" viewBox="0 0 20 20"><path d="M10 3 C5 3 5 9 4 13 L16 13 C15 9 15 3 10 3 Z" fill="#3aaa35"/><rect x="3" y="13" width="14" height="2.5" rx="1" fill="#3aaa35"/><circle cx="10" cy="17.5" r="1.8" fill="#3aaa35"/></svg>
    </div>
    <div class="occasion-title">Christmas</div>
    <div class="occasion-link">View all christmas gifts</div>
    <div class="occasion-text">Ut congue ut lectus a lobortis<br>aenean iaculis sem est,</div>
  </div>
  <div class="occasion" style="left:607px">
    <div class="occasion-icon">
      <svg width="20" height="20" viewBox="0 0 20 20"><path d="M10 17 L3 10 A4 4 0 0 1 10 5 A4 4 0 0 1 17 10 Z" fill="#e8352f"/></svg>
    </div>
    <div class="occasion-title">Valentine’s Day</div>
    <div class="occasion-link">View all valentine gifts</div>
    <div class="occasion-text">Ut congue ut lectus a lobortis<br>aenean iaculis sem est,</div>
  </div>
</section>

<div class="rule" style="top:544px"></div>

<section>
  <div class="product" style="left:184px; top:569px">
    <div class="product-frame"><div class="product-photo" role="img" aria-label="Stacked white gift boxes with orange tissue and chocolates" style="background:linear-gradient(180deg,#f5c68a,#f0efe9 60%,#e8a860)"></div></div>
    <div class="product-row"><span>Tower of Temptation</span><span class="product-price">$64.95</span></div>
    <div class="product-meta"><span>Birthday</span><span class="ship">Free Shipping</span></div>
  </div>
  <div class="product" style="left:398px; top:569px">
    <div class="product-frame"><div class="product-photo" role="img" aria-label="Bouquet of gold-wrapped chocolates in purple paper" style="width:120px;height:100px;background:radial-gradient(ellipse at 50% 40%,#a9883a,#6b5420 60%,#5b3c8a 100%);border-radius:40%"></div></div>
    <div class="product-row"><span>Hazelnut Truffle Bouquet</span><span class="product-price">$69.00</span></div>
    <div class="product-meta"><span>For Him</span><span class="ship">Free Shipping</span></div>
  </div>
  <div class="product" style="left:612px; top:569px">
    <div class="product-frame"><div class="product-photo" role="img" aria-label="Herb plants, cheese and crackers gift set in a red box" style="width:110px;background:linear-gradient(180deg,#2f5a2a 0%,#3d6f30 45%,#c9302c 60%,#b89a70 100%)"></div></div>
    <div class="product-row"><span>Herb Cheese &amp; Cracker Present</span><span class="product-price">$59.95</span></div>
    <div class="product-meta"><span>Christmas</span><span class="ship">Free Shipping</span></div>
  </div>

  <div class="product" style="left:184px; top:770px">
    <div class="product-frame"><div class="product-photo" role="img" aria-label="Stacked white gift boxes with orange tissue and chocolates" style="background:linear-gradient(180deg,#f5c68a,#f0efe9 60%,#e8a860)"></div></div>
    <div class="product-row"><span>Tower of Temptation</span><span class="product-price">$64.95</span></div>
    <div class="product-meta"><span>Birthday</span><span class="ship">Free Shipping</span></div>
  </div>
  <div class="product" style="left:398px; top:770px">
    <div class="product-frame"><div class="product-photo" role="img" aria-label="Bouquet of gold-wrapped chocolates in purple paper" style="width:120px;height:100px;background:radial-gradient(ellipse at 50% 40%,#a9883a,#6b5420 60%,#5b3c8a 100%);border-radius:40%"></div></div>
    <div class="product-row"><span>Hazelnut Truffle Bouquet</span><span class="product-price">$69.00</span></div>
    <div class="product-meta"><span>For Him</span><span class="ship">Free Shipping</span></div>
  </div>
  <div class="product" style="left:612px; top:770px">
    <div class="product-frame"><div class="product-photo" role="img" aria-label="Herb plants, cheese and crackers gift set in a red box" style="width:110px;background:linear-gradient(180deg,#2f5a2a 0%,#3d6f30 45%,#c9302c 60%,#b89a70 100%)"></div></div>
    <div class="product-row"><span>Herb Cheese &amp; Cracker Present</span><span class="product-price">$59.95</span></div>
    <div class="product-meta"><span>Christmas</span><span class="ship">Free Shipping</span></div>
  </div>
</section>

<div class="rule" style="top:971px"></div>

<section>
  <div class="seo">
    <h2>Lorem Ipsum Dolor Sit Amet</h2>
    <p>Nam pellentesque mi nibh, porttitor egestas urna viverra et. Curabitur enim justo, blandit in pharetra id, facilisis sit amet arcu. Vivamus hendrerit felis vel nulla facilisis, et sollicitudin urna congue. Cras nec tellus fermentum, dignissim nisl eu, malesuada nisi.</p>
  </div>
  <div class="seo-photo" role="img" aria-label="Christmas tree with glowing lights against a blue night sky" style="left:517px; background:radial-gradient(circle at 45% 60%,#c0452a,#5a3a3a 45%,#1f4a6e 80%)"></div>
  <div class="seo-photo" role="img" aria-label="Close-up of an orange sunflower" style="left:661px; background:radial-gradient(circle at 50% 50%,#5a3a12,#c46a14 45%,#e8a020 80%)"></div>
</section>

<div class="rule" style="top:1122px"></div>

<footer>
  <div class="footer-links"><span>Term and Conditions</span><span>Privacy</span><span>About Us</span><span>Contact</span><span>Shipping</span></div>
  <div class="copyright">© Parcelnook.com.au 2014. Gift Baskets &amp; Hampers delivered throughout Australia. All prices in USD.</div>
  <div class="footer-band"></div>
</footer>

</body>
</html>
```